Geschäftspapiere für Kanzlei
Zielgruppe
Forschungsinstitute und Großunternehmen die eigene Entwicklungsabteilungen haben und Erfindungen patentieren lassen.
Aufgabenstellung
Möglicherweise ergibt eine Weiterentwiklung unseres logos Sinn? Denkbar wäre für uns aber auch auf das Logo ganz zu verzichten.
Es sollte nicht mehr als eine Farbe (Blauton) verwendet werden. Wir wollen schlicht, klassisch und seriös auftreten.

```html
<!DOCTYPE html>
<html lang="de">
<head>
<meta charset="utf-8">
<title>Briefbogen – Patentanwaltskanzlei Dr. Markhoff</title>
<link rel="stylesheet" href="https://fonts.googleapis.com/css2?family=EB+Garamond:wght@600&family=Libre+Franklin:wght@400&display=swap">
<style>
  :root {
    --backdrop: #c6c6c6;
    --paper: #f4f4f4;
    --brand-blue: #1d3461;
    --ink: #2a2a2a;
  }
  * { margin: 0; padding: 0; box-sizing: border-box; }
  html, body {
    width: 1200px;
    height: 860px;
    overflow: hidden;
    background: var(--backdrop);
  }
  .letterhead {
    position: absolute;
    left: 310px;
    top: 20px;
    width: 580px;
    height: 820px;
    background: var(--paper);
    box-shadow: 0 2px 10px rgba(0,0,0,0.15);
    font-family: "Libre Franklin", Arial, sans-serif;
    color: var(--ink);
  }
  .brand {
    position: absolute;
    left: 58px;
    top: 58px;
    display: flex;
    align-items: center;
    gap: 12px;
  }
  .brand-square {
    width: 14px;
    height: 14px;
    background: var(--brand-blue);
  }
  .brand-text { color: var(--brand-blue); }
  .brand-name {
    font-family: "EB Garamond", Georgia, serif;
    font-weight: 600;
    font-size: 19px;
    letter-spacing: 1px;
    text-transform: uppercase;
    line-height: 1.1;
  }
  .brand-tagline {
    font-size: 8.5px;
    letter-spacing: 3px;
    text-transform: uppercase;
    margin-top: 3px;
  }
  .sender-line {
    position: absolute;
    left: 58px;
    top: 182px;
    font-size: 8px;
  }
  .contact-block {
    position: absolute;
    left: 405px;
    top: 182px;
    font-size: 7px;
    line-height: 1.35;
  }
  .contact-block p + p { margin-top: 8px; }
  .footer {
    position: absolute;
    left: 0;
    right: 0;
    bottom: 36px;
    text-align: center;
    font-size: 7.5px;
    line-height: 1.4;
  }
</style>
</head>
<body>
  <main class="letterhead">
    <header class="brand">
      <span class="brand-square"></span>
      <div class="brand-text">
        <div class="brand-name">Dr. Elias Markhoff</div>
        <div class="brand-tagline">Patentanwaltskanzlei</div>
      </div>
    </header>

    <div class="sender-line">Kanzlei Dr. Markhoff • Kastanienweg 27 • 80469 München</div>

    <aside class="contact-block">
      <p>Dr. rer. nat. Elias Markhoff, PhD<br>
        Patentanwalt<br>
        European Patent Attorney<br>
        European Design- und Trademark Attorney</p>
      <p>Kastanienweg 27<br>
        80469 München</p>
      <p>Tel.: + 49 89 400 118 230<br>
        Fax: + 49 89 400 118 39<br>
        Email: office@markhoff-patent.de</p>
    </aside>

    <footer class="footer">
      Patentanwaltskanzlei Dr. Markhoff, Steuernummer.: 143/275/80319, www.markhoff-patent.de<br>
      Nordbank Süd, UStID Nummer, IBAN: DE00123400009876543210, BIC: NOSUDEM1XXX
    </footer>
  </main>
</body>
</html>
```